Yoga Instrucor

I need my personal business cards, i would like the front a kind of light but vibrant red and matt gold.

Industry/Entity Type

Business

Contact Information for Business Card

Cordelia Hastrup
Yoga Instructor
RYT 200, BROKU (NYC) Yoga RYT 500,
CPR/ AED Certified,
hastrupcordelia@quillbox.com
512 604 8893
Adult Yoga, Private Yoga, Group Classes, Restorative, Meditation, Child Yoga.

```html
<!DOCTYPE html>
<html lang="en">
<head>
<meta charset="utf-8">
<title>Cordelia Hastrup – Yoga Instructor Business Card</title>
<link rel="stylesheet" href="https://fonts.googleapis.com/css2?family=Quicksand:wght@400;500;600&display=swap">
<style>
  :root {
    --page: #ffffff;
    --gold: #f7c64f;
    --gold-soft: #f3cf74;
    --wood-dark: #4a1d0c;
    --wood-mid: #7a3413;
    --flame: #f07a1c;
    --sun: #ffd23a;
    --red-deep: #a8101a;
    --red-bright: #ec1c2a;
    --red-ornament: #8e0d15;
  }
  * { margin: 0; padding: 0; box-sizing: border-box; }
  html, body {
    width: 942px;
    height: 1200px;
    overflow: hidden;
    background: var(--page);
    font-family: "Quicksand", "Trebuchet MS", sans-serif;
  }
  .sheet { position: relative; width: 942px; height: 1200px; }
  .card {
    position: absolute;
    left: 69px;
    width: 819px;
    height: 465px;
    overflow: hidden;
  }
  .card--front { top: 80px; }
  .card--back { top: 627px; }

  .front-art {
    position: absolute;
    inset: 0;
    background:
      radial-gradient(ellipse 300px 260px at 700px 190px, var(--sun) 0%, #f9a52a 45%, rgba(240,122,28,0) 80%),
      radial-gradient(ellipse 260px 300px at 420px 180px, rgba(246,170,80,.9) 0%, rgba(240,122,28,.6) 45%, rgba(240,122,28,0) 80%),
      linear-gradient(90deg, var(--wood-dark) 0%, var(--wood-mid) 35%, var(--flame) 70%, #f59a2a 100%);
  }
  .services {
    position: absolute;
    left: 0;
    width: 406px;
    top: 322px;
    text-align: center;
    color: var(--gold);
    font-size: 22px;
    font-weight: 500;
    line-height: 32px;
  }

  .back-bg {
    position: absolute;
    inset: 0;
    background: linear-gradient(90deg, var(--red-deep) 0%, #d0141f 30%, var(--red-bright) 55%, #c8121d 100%);
  }
  .back-ornament {
    position: absolute;
    left: 500px;
    top: -20px;
    width: 360px;
    height: 500px;
    border-radius: 50%;
    background: radial-gradient(ellipse at center, var(--red-bright) 0%, #b50f1a 35%, var(--red-ornament) 65%, rgba(142,13,21,0) 72%);
  }
  .name {
    position: absolute;
    left: 46px;
    top: 103px;
    color: var(--gold);
    font-size: 34px;
    font-weight: 500;
    letter-spacing: .5px;
  }
  .name-rule {
    position: absolute;
    left: 46px;
    top: 157px;
    width: 360px;
    height: 2px;
    background: var(--gold-soft);
  }
  .credentials {
    position: absolute;
    left: 46px;
    top: 170px;
    list-style: none;
    color: var(--gold);
    font-size: 19px;
    font-weight: 500;
    line-height: 28px;
  }
  .contact {
    position: absolute;
    left: 46px;
    color: var(--gold);
    display: flex;
    align-items: center;
    gap: 8px;
  }
  .contact--phone { top: 332px; font-size: 29px; font-weight: 500; }
  .contact--email { top: 370px; font-size: 21px; font-weight: 400; }
  .contact svg { fill: var(--gold); flex: none; }
</style>
</head>
<body>
<main class="sheet">
  <section class="card card--front">
    <div class="front-art" role="img" aria-label="Illustration of a yoga figure in tree pose with orange petals and a glowing swirl sun over a wood background"></div>
    <p class="services">Adult Yoga, Private Yoga,<br>Group Classes, Restorative<br>Meditation, Child Yoga</p>
  </section>

  <section class="card card--back">
    <div class="back-bg"></div>
    <div class="back-ornament" role="img" aria-label="Decorative dark red swirl mandala with a small red flower"></div>
    <h1 class="name">Cordelia Hastrup</h1>
    <div class="name-rule"></div>
    <ul class="credentials">
      <li>YOGA INSTRUCTOR RYT 200</li>
      <li>BROKU (NYC) YOGA RYT 500</li>
      <li>CPR/ AED CERTIFIED</li>
    </ul>
    <p class="contact contact--phone">
      <svg width="24" height="26" viewBox="0 0 24 24" aria-hidden="true"><path d="M6.6 10.8c1.4 2.8 3.8 5.1 6.6 6.6l2.2-2.2c.3-.3.7-.4 1-.2 1.1.4 2.3.6 3.6.6.6 0 1 .4 1 1V20c0 .6-.4 1-1 1C10.6 21 3 13.4 3 4c0-.6.4-1 1-1h3.5c.6 0 1 .4 1 1 0 1.3.2 2.5.6 3.6.1.3 0 .7-.2 1z"/></svg>
      512 604 8893
    </p>
    <p class="contact contact--email">
      <svg width="22" height="18" viewBox="0 0 22 18" aria-hidden="true"><path d="M1 2h20v14H1z M2.5 3.5 11 10l8.5-6.5z" fill-rule="evenodd"/></svg>
      hastrupcordelia@quillbox.com
    </p>
  </section>
</main>
</body>
</html>
```